Bref créative
logo for mining tool supplier
Durable Quarry Fittings
Professional
Luka Vranek
Manager
42 Tindale ave
Wirrabong NSW 2581
sales@quarry-fittings.com.au
quarry-fittings.com.au

```html
<!DOCTYPE html>
<html lang="en">
<head>
<meta charset="utf-8">
<title>Durable Quarry Fittings – Business Card</title>
<link rel="stylesheet" href="https://fonts.googleapis.com/css2?family=Open+Sans:wght@400;600;700&display=swap">
<style>
  :root {
    --backdrop: #e9e6e1;
    --card: #ffffff;
    --brand-orange: #f47a20;
    --soft-orange: #f6a45f;
    --ink-grey: #5b5b5b;
    --name-grey: #4a5560;
  }
  * { margin: 0; padding: 0; box-sizing: border-box; }
  html, body {
    width: 1200px; height: 914px; overflow: hidden;
    background: var(--backdrop);
    font-family: "Open Sans", Arial, sans-serif;
  }
  .canvas {
    width: 1200px; height: 914px;
    display: flex; align-items: center; justify-content: center;
  }
  .business-card {
    position: relative;
    width: 1000px; height: 600px;
    background: var(--card);
    box-shadow: 0 10px 30px rgba(0,0,0,.12);
  }
  .brand {
    position: absolute; top: 210px; left: 0; right: 0;
    display: flex; justify-content: center; align-items: center; gap: 16px;
  }
  .brand-mark {
    width: 30px; height: 30px; border-radius: 50%;
    background: var(--brand-orange);
  }
  .brand-name {
    font-size: 42px; font-weight: 600; line-height: 1;
    color: var(--name-grey);
  }
  .person {
    position: absolute; top: 380px; left: 0; right: 0;
    text-align: center; font-size: 22px;
  }
  .person-name { font-weight: 700; color: var(--brand-orange); }
  .person-divider { color: var(--ink-grey); margin: 0 6px; }
  .person-role { color: var(--soft-orange); }
  .contacts {
    position: absolute; top: 440px; left: 180px; right: 120px;
    display: grid; grid-template-columns: auto auto; column-gap: 40px; row-gap: 10px;
    font-size: 18px; color: var(--ink-grey);
  }
  .contact { display: flex; align-items: center; gap: 8px; white-space: nowrap; }
  .contact svg { width: 20px; height: 20px; flex: none; }
</style>
</head>
<body>
<div class="canvas">
  <div class="business-card">
    <div class="brand">
      <span class="brand-mark"></span>
      <span class="brand-name">Durable Quarry Fittings</span>
    </div>

    <div class="person">
      <span class="person-name">Luka Vranek</span><span class="person-divider">|</span><span class="person-role">Manager</span>
    </div>

    <div class="contacts">
      <div class="contact">
        <svg viewBox="0 0 20 20"><circle cx="10" cy="10" r="10" fill="#f47a20"/><path d="M10 4a4 4 0 0 0-4 4c0 3 4 8 4 8s4-5 4-8a4 4 0 0 0-4-4zm0 5.5a1.5 1.5 0 1 1 0-3 1.5 1.5 0 0 1 0 3z" fill="#fff"/></svg>
        <span>42 Tindale ave Wirrabong NSW 2581</span>
      </div>
      <div class="contact">
        <svg viewBox="0 0 20 20"><circle cx="10" cy="10" r="10" fill="#f47a20"/><circle cx="10" cy="10" r="5.5" fill="none" stroke="#fff" stroke-width="1.4"/><path d="M4.5 10h11M10 4.5c-2.5 3-2.5 8 0 11M10 4.5c2.5 3 2.5 8 0 11" fill="none" stroke="#fff" stroke-width="1.2"/></svg>
        <span>quarry-fittings.com.au</span>
      </div>
      <div class="contact">
        <svg viewBox="0 0 20 20"><circle cx="10" cy="10" r="10" fill="#f47a20"/><path d="M7 5l2 2.5-1.2 1.5a7 7 0 0 0 3.2 3.2L12.5 11 15 13l-1 2c-4.5 0-9-4.5-9-9z" fill="#fff"/></svg>
        <span>0412 587 306</span>
      </div>
      <div class="contact">
        <svg viewBox="0 0 20 20"><circle cx="10" cy="10" r="10" fill="#f47a20"/><rect x="5" y="6.5" width="10" height="7" rx="1" fill="#fff"/><path d="M5.5 7l4.5 3.5L14.5 7" fill="none" stroke="#f47a20" stroke-width="1.2"/></svg>
        <span>sales@quarry-fittings.com.au</span>
      </div>
    </div>
  </div>
</div>
</body>
</html>
```